Awesome photographers card for an awesome new business

Double sided business card Black background and silver logo in middle on one side. Details on otherside. please keep it simple

Photographer

Gavin Tolley
0482615073
GavinTolleyPhotography82@lumenpost.com
www.GavinTolleyPhotography.com.au
Instagram _Gavin_tolley

Requirements
Must have
• My logo in Silver
• please use instagram logo instead of "Instagram"

```html
<!DOCTYPE html>
<html lang="en">
<head>
<meta charset="utf-8">
<title>Gavin Tolley Photographer – Business Card</title>
<link rel="stylesheet" href="https://fonts.googleapis.com/css2?family=Quicksand:wght@400;500&display=swap">
<style>
  :root {
    --page: #ffffff;
    --card-black: #151515;
    --ink-white: #ffffff;
    --silver: #9a9a9a;
    --graphite: #5f605f;
    --camera-dark: #0b0b0b;
    --lens-black: #111111;
  }
  * { margin: 0; padding: 0; box-sizing: border-box; }
  html, body {
    width: 1200px;
    height: 1200px;
    overflow: hidden;
    background: var(--page);
    font-family: "Quicksand", sans-serif;
  }
  .canvas { position: relative; width: 1200px; height: 1200px; }

  /* Front side */
  .card-front {
    position: absolute;
    left: 266px;
    top: 62px;
    width: 840px;
    height: 480px;
    overflow: hidden;
  }
  .camera-artwork {
    position: absolute;
    inset: 0;
    background: linear-gradient(180deg,
      var(--camera-dark) 0%,
      var(--camera-dark) 12%,
      var(--silver) 20%,
      var(--lens-black) 35%,
      var(--lens-black) 70%,
      var(--silver) 85%,
      var(--graphite) 100%);
  }
  .logo-mark {
    position: absolute;
    left: 304px;
    top: 88px;
    width: 356px;
    height: 356px;
    border-radius: 50%;
    background: var(--lens-black);
    border: 14px solid var(--ink-white);
    display: flex;
    align-items: center;
    justify-content: center;
  }
  .logo-name {
    color: var(--silver);
    font-weight: 500;
    font-size: 40px;
    letter-spacing: 1px;
    white-space: nowrap;
  }

  /* Back side */
  .card-back {
    position: absolute;
    left: 102px;
    top: 614px;
    width: 840px;
    height: 480px;
    background: var(--card-black);
    color: var(--ink-white);
    overflow: hidden;
  }
  .frame-corners { position: absolute; inset: 0; }
  .identity {
    position: absolute;
    right: 98px;
    top: 52px;
    text-align: right;
    font-weight: 400;
  }
  .identity-name { font-size: 62px; line-height: 80px; }
  .identity-role { font-size: 38px; line-height: 52px; margin-top: 4px; }
  .identity-web { font-size: 25px; line-height: 34px; margin-top: 24px; letter-spacing: 0.2px; }

  .contact-list {
    position: absolute;
    left: 91px;
    top: 296px;
    list-style: none;
  }
  .contact-item {
    display: flex;
    align-items: center;
    height: 42px;
    font-size: 21px;
  }
  .contact-icon { width: 29px; height: 29px; margin-right: 11px; flex: none; }
</style>
</head>
<body>
<main class="canvas">

  <section class="card-front" aria-label="Business card front">
    <div class="camera-artwork" role="img" aria-label="Stylised grey and black camera body illustration"></div>
    <div class="logo-mark">
      <span class="logo-name">Gavin Tolley</span>
    </div>
  </section>

  <section class="card-back" aria-label="Business card back">
    <svg class="frame-corners" width="840" height="480" viewBox="0 0 840 480" aria-hidden="true">
      <g fill="none" stroke="#ffffff" stroke-width="4">
        <path d="M71 115 V42 H144"/>
        <path d="M702 42 H775 V115"/>
        <path d="M71 362 V434 H144"/>
        <path d="M702 434 H775 V362"/>
      </g>
    </svg>

    <div class="identity">
      <h1 class="identity-name">Gavin Tolley</h1>
      <p class="identity-role">photographer</p>
      <p class="identity-web">www.GavinTolleyPhotography.com.au</p>
    </div>

    <ul class="contact-list">
      <li class="contact-item">
        <svg class="contact-icon" viewBox="0 0 29 29" aria-hidden="true">
          <circle cx="14.5" cy="14.5" r="14" fill="#ffffff"/>
          <rect x="6.5" y="9" width="16" height="11" fill="none" stroke="#151515" stroke-width="1.6"/>
          <path d="M6.5 9 L14.5 15.5 L22.5 9 M6.5 20 L12 14 M22.5 20 L17 14" fill="none" stroke="#151515" stroke-width="1.4"/>
        </svg>
        <span>GavinTolleyPhotography82@lumenpost.com</span>
      </li>
      <li class="contact-item">
        <svg class="contact-icon" viewBox="0 0 29 29" aria-hidden="true">
          <path d="M14.5 2 L28 27 H1 Z" fill="#ffffff" stroke="#ffffff" stroke-width="2" stroke-linejoin="round"/>
          <path d="M10 13 c-1 2 2 8 7 10 l2.5-2.5 -3-2 -1.5 1.2 c-1.5-.8-3-2.8-3.4-4.3 l1.3-1.2 -1.6-3 Z" fill="#151515"/>
        </svg>
        <span>0482615073</span>
      </li>
      <li class="contact-item">
        <svg class="contact-icon" viewBox="0 0 29 29" aria-hidden="true">
          <rect x="2" y="2" width="25" height="25" rx="5" fill="#ffffff"/>
        </svg>
        <span>_Gavin_tolley</span>
      </li>
    </ul>
  </section>

</main>
</body>
</html>
```